Divorce marketing brochure - Which will include a toy ball and chain as a gimick

A single page marketing enclosure which includes a toy ball and chain to be given to lawyers. I want to convey the following messages:

1. We pay a 1/3 referral fee;
2. We solve difficult problems.

Examples of problems solved:
*Litigation of complex property, custody, support and parenting time issues;
*Protection (or invasion) of personal injury proceeds in divorce;
*Distribution of consortium proceeds in divorce;
*Pre-nuptial and Post-nuptial agreements.
*Settlements
*Reduce conflict

A sample of the toy ball and chain enclosure can be viewed here:

My website is www.thesplitcounsel.com (currently being updated - who's isn't?)

http://www.shopvarnex.com/Pelbrook-Gadgets-Inc-Convict-Shackle/dp/Q7K4TZ2MXA/ref=sr_1_9?ie=UTF8&qid=1311011554&sr=8-9

Target Market(s)

Personal Injury Attorneys

Industry/Entity Type

Marketing

Requirements
Must have
• Call to action:

www.thesplitcounsel.com
1-866-LAWS-DESK
517-624-8107
Marcus@brevanolegal.com
Nice to have
• I want this campaign to stand out. Different is good. I am a divorce lawyer marketing to personal injury attorneys (and some others) for divorce referrals. (No one forgets the girl with red hair and braces) I want the campaign to be remembered without being offensive.
Should not have

```html
<!DOCTYPE html>
<html lang="en">
<head>
<meta charset="utf-8">
<title>The Split Counsel – Referral Brochure</title>
<link rel="stylesheet" href="https://fonts.googleapis.com/css2?family=Archivo+Black&family=Arimo:wght@400;700&display=swap">
<style>
  :root {
    --navy: #1d1a6b;
    --band-dark: #1f1c78;
    --band-mid: #3a37a6;
    --band-light: #5a58c4;
    --band-edge: #c8c6e4;
    --lavender: #8479c6;
    --note-yellow: #fbf9cc;
    --key-tan: #c9c29a;
    --cream: #f6f1b6;
    --white: #ffffff;
    --ink: #111111;
    --skin: #c99c80;
    --iron: #4a4a4f;
  }
  * { margin: 0; padding: 0; box-sizing: border-box; }
  html, body { width: 848px; height: 1200px; overflow: hidden; background: var(--white); }
  .brochure {
    position: relative;
    width: 848px;
    height: 1200px;
    overflow: hidden;
    background: var(--white);
    font-family: "Arimo", Arial, sans-serif;
  }
  .masthead {
    position: absolute; left: 0; top: 0; width: 100%; height: 130px;
    background: linear-gradient(180deg, var(--band-dark) 0%, var(--band-mid) 100%);
  }
  .masthead-name {
    position: absolute; left: 0; right: 0; top: 30px;
    text-align: center;
    font-family: "Archivo Black", "Arial Black", sans-serif;
    font-size: 50px; letter-spacing: 0.5px;
    color: var(--cream);
  }
  .sheen {
    position: absolute; left: 0; top: 130px; width: 100%; height: 40px;
    background: linear-gradient(180deg, #d8d8de 0%, var(--white) 100%);
  }
  .headline {
    position: absolute; left: 0; right: 0; top: 186px;
    text-align: center;
    font-family: "Archivo Black", "Arial Black", sans-serif;
    font-weight: 400;
    font-size: 47px; line-height: 60px;
    color: var(--navy);
  }
  .headline .accent { color: var(--lavender); }
  .problems {
    position: absolute; left: 245px; top: 338px; width: 585px; height: 536px;
    background: var(--note-yellow);
  }
  .problems-title {
    position: absolute; left: 300px; top: 380px;
    font-family: "Arimo", Arial, sans-serif; font-weight: 700;
    font-size: 25px; color: var(--lavender);
  }
  .problem-list { list-style: none; position: absolute; left: 210px; top: 440px; width: 560px; }
  .problem-item {
    position: relative; padding-left: 89px;
    font-size: 19.5px; line-height: 25px; color: var(--ink);
  }
  .problem-item .key { position: absolute; left: 0; top: 4px; width: 72px; height: 18px; }
  .item-1, .item-2 { height: 86px; }
  .item-3, .item-4, .item-5 { height: 54px; }
  .shackle-photo {
    position: absolute; left: 0; top: 822px; width: 790px; height: 126px;
    background: linear-gradient(90deg, var(--skin) 0%, #b89a88 28%, #7d7a80 55%, var(--iron) 100%);
  }
  .footer-band {
    position: absolute; left: 0; top: 948px; width: 100%; height: 252px;
    background: linear-gradient(180deg, var(--band-edge) 0px, var(--band-edge) 10px, var(--band-mid) 12px, var(--band-light) 60px, var(--band-dark) 100%);
  }
  .contact {
    position: absolute; right: 16px; top: 1054px;
    text-align: right; color: var(--white);
    font-style: normal;
    font-size: 19.5px; line-height: 28px;
  }
  .contact-web { font-weight: 700; font-size: 24px; color: var(--cream); line-height: 32px; }
</style>
</head>
<body>
<main class="brochure">
  <header class="masthead">
    <div class="masthead-name">thesplitcounsel.com</div>
  </header>
  <div class="sheen"></div>

  <h1 class="headline">
    We pay <span class="accent">a 1/3 referral fee</span><br>
    We solve <span class="accent">difficult problems</span>
  </h1>

  <section class="problems" aria-labelledby="problems-title"></section>
  <h2 class="problems-title" id="problems-title">Examples of problems solved:</h2>
  <ul class="problem-list">
    <li class="problem-item item-1"><svg class="key" viewBox="0 0 72 18" aria-hidden="true"><rect x="0" y="7" width="46" height="4" fill="var(--key-tan)"/><rect x="6" y="11" width="4" height="5" fill="var(--key-tan)"/><rect x="14" y="11" width="4" height="4" fill="var(--key-tan)"/><circle cx="58" cy="9" r="8.5" fill="var(--key-tan)"/><circle cx="61" cy="9" r="3" fill="var(--note-yellow)"/></svg>Litigation of complex property, custody,<br>support and parenting time issues</li>
    <li class="problem-item item-2"><svg class="key" viewBox="0 0 72 18" aria-hidden="true"><rect x="0" y="7" width="46" height="4" fill="var(--key-tan)"/><rect x="6" y="11" width="4" height="5" fill="var(--key-tan)"/><rect x="14" y="11" width="4" height="4" fill="var(--key-tan)"/><circle cx="58" cy="9" r="8.5" fill="var(--key-tan)"/><circle cx="61" cy="9" r="3" fill="var(--note-yellow)"/></svg>Protection (or invasion) of personal injury<br>proceeds in divorce</li>
    <li class="problem-item item-3"><svg class="key" viewBox="0 0 72 18" aria-hidden="true"><rect x="0" y="7" width="46" height="4" fill="var(--key-tan)"/><rect x="6" y="11" width="4" height="5" fill="var(--key-tan)"/><rect x="14" y="11" width="4" height="4" fill="var(--key-tan)"/><circle cx="58" cy="9" r="8.5" fill="var(--key-tan)"/><circle cx="61" cy="9" r="3" fill="var(--note-yellow)"/></svg>Distribution of consortium proceeds in divorce</li>
    <li class="problem-item item-4"><svg class="key" viewBox="0 0 72 18" aria-hidden="true"><rect x="0" y="7" width="46" height="4" fill="var(--key-tan)"/><rect x="6" y="11" width="4" height="5" fill="var(--key-tan)"/><rect x="14" y="11" width="4" height="4" fill="var(--key-tan)"/><circle cx="58" cy="9" r="8.5" fill="var(--key-tan)"/><circle cx="61" cy="9" r="3" fill="var(--note-yellow)"/></svg>Pre-nuptial and Post-nuptial agreements</li>
    <li class="problem-item item-5"><svg class="key" viewBox="0 0 72 18" aria-hidden="true"><rect x="0" y="7" width="46" height="4" fill="var(--key-tan)"/><rect x="6" y="11" width="4" height="5" fill="var(--key-tan)"/><rect x="14" y="11" width="4" height="4" fill="var(--key-tan)"/><circle cx="58" cy="9" r="8.5" fill="var(--key-tan)"/><circle cx="61" cy="9" r="3" fill="var(--note-yellow)"/></svg>Settlements</li>
    <li class="problem-item item-6"><svg class="key" viewBox="0 0 72 18" aria-hidden="true"><rect x="0" y="7" width="46" height="4" fill="var(--key-tan)"/><rect x="6" y="11" width="4" height="5" fill="var(--key-tan)"/><rect x="14" y="11" width="4" height="4" fill="var(--key-tan)"/><circle cx="58" cy="9" r="8.5" fill="var(--key-tan)"/><circle cx="61" cy="9" r="3" fill="var(--note-yellow)"/></svg>Reduce conflict</li>
  </ul>

  <div class="shackle-photo" role="img" aria-label="Photo of a bare foot in an iron shackle chained to a heavy black ball"></div>
  <div class="footer-band"></div>

  <address class="contact">
    <div class="contact-web">www.thesplitcounsel.com</div>
    <div>1-866-LAWS-DESK</div>
    <div>517-624-8107</div>
    <div>Marcus@brevanolegal.com</div>
  </address>
</main>
</body>
</html>
```